Graphic Design Project

Intranet home page design. Current design is bland and amateurish.

I want a new design that looks like it belongs to a Meridian 300 company! Top shelf and very professional.

Must have all menu items of existing home page - see uploaded jpg file.
Updates

Please note that the company logo must stay the same, but you can change the colors if you like.

Thank you all for helping me!

Industry/Entity Type

Graphic Design

Requirements
Must have
• Must have all menu items of existing home page - see uploaded jpg file.

```html
<!DOCTYPE html>
<html lang="en">
<head>
<meta charset="utf-8">
<title>Harlow &amp; Reed Intranet – Home</title>
<link rel="stylesheet" href="https://fonts.googleapis.com/css2?family=Arimo:wght@400;700&family=Montserrat:wght@400&family=Gochi+Hand&display=swap">
<style>
:root{
  --navy:#27365f;
  --navy-mid:#3b4a7a;
  --nav-btn:#3e4f80;
  --brand:#2c3e6b;
  --page-grey:#dcdce2;
  --lilac:#b9aedb;
  --lilac-deep:#9b8fc9;
  --lilac-tab:#a294d0;
  --band:#a89ecd;
  --card:#b8afd9;
  --pill:#9a8fc6;
  --ink:#2a2140;
  --cal-cell:#c9ccdc;
  --cal-btn:#6d7199;
  --note:#e2261f;
  --white:#ffffff;
}
*{margin:0;padding:0;box-sizing:border-box}
html,body{width:1200px;height:501px;overflow:hidden;background:var(--white)}
body{position:relative;font-family:"Arimo",Arial,sans-serif;color:var(--ink)}
.screen{position:absolute;top:0;height:501px}
.screen--closed{left:0;width:568px}
.screen--open{left:600px;width:596px}
.screen > *{position:absolute}

.brand{left:16px;top:62px;display:flex;align-items:center;gap:8px}
.brand__dot{width:46px;height:46px;border-radius:50%;background:var(--brand)}
.brand__name{font-weight:700;font-size:21px;color:var(--brand);letter-spacing:.5px;width:120px;line-height:21px}
.site-title{left:236px;top:74px;font-family:"Montserrat",sans-serif;font-size:20px;letter-spacing:5px;color:#222}

.logout{top:108px;right:2px;width:48px;height:12px;border-radius:6px 6px 0 0;background:var(--navy-mid);color:var(--white);font-size:7px;text-align:center;line-height:12px}
.topbar{left:0;right:0;top:119px;height:7px;background:var(--navy)}
.page{left:0;right:0;top:126px;height:220px;background:var(--page-grey)}

.nav{top:128px;left:68px;display:flex;gap:1px}
.nav__item{height:20px;background:var(--nav-btn);color:var(--white);font-size:5.6px;line-height:6px;text-align:center;display:flex;align-items:center;justify-content:center;width:37px}
.nav__item--wide{width:46px}
.tab{top:128px;right:2px;width:62px;height:24px;background:var(--lilac);font-size:7.5px;color:var(--ink);text-align:center;line-height:20px}
.screen--open .tab{right:30px;height:28px}

.news{top:156px;left:10px;height:184px;background:var(--lilac);border-radius:6px;padding:18px 8px 0 8px}
.screen--closed .news{width:546px}
.screen--open .news{width:360px}
.news__title{position:absolute;left:3px;top:2px;padding:0 8px;height:14px;background:var(--lilac-tab);color:var(--white);font-size:11.5px;line-height:14px;border-radius:3px 10px 0 0}
.news h3{font-size:9px;text-align:right;margin-bottom:2px}
.news p{font-size:7.4px;line-height:9.4px;margin-bottom:10px}
.screen--open .news p{font-size:7.2px;line-height:9.4px;margin-bottom:8px}

.personal{top:157px;left:372px;width:193px;height:183px;border:6px solid var(--lilac-deep);border-radius:10px;background:var(--lilac)}
.calendar{position:absolute;left:4px;top:4px;width:173px;height:108px;background:var(--white);border-radius:4px;display:flex;padding:3px}
.calendar__grid{display:grid;grid-template-columns:repeat(7,20px);grid-auto-rows:14px;gap:1px;font-size:7px;text-align:center}
.calendar__day{font-weight:700;line-height:14px}
.calendar__date{line-height:13px;border:1px solid #aab}
.calendar__date--busy{background:var(--cal-cell)}
.calendar__blank{}
.calendar__month{margin-left:6px;width:14px;background:var(--navy-mid);border-radius:7px;color:var(--white);font-size:7.5px;writing-mode:vertical-rl;text-align:center;letter-spacing:2px;line-height:14px}
.actions{position:absolute;left:4px;top:118px;display:grid;grid-template-columns:84px 84px;gap:5px}
.actions__btn{height:18px;background:var(--cal-btn);color:var(--white);font-size:7.5px;text-align:center;line-height:18px;border-radius:3px}

.band{left:0;right:0;top:346px;height:122px;background:linear-gradient(var(--band),#b4abd6)}
.card{top:360px;width:136px;height:90px;background:var(--card);border-radius:4px;font-size:7.5px;line-height:9px;text-align:center;padding-top:8px;color:var(--white)}
.pill{top:452px;width:128px;height:14px;background:var(--pill);border-radius:3px;color:var(--white);font-size:7.5px;text-align:center;line-height:14px}
.video{top:362px;width:133px;height:87px;background:linear-gradient(135deg,#6b5a52,#b39a86);border-radius:3px}
.video__play{position:absolute;left:56px;top:33px;width:22px;height:16px;border-radius:3px;background:#111}
.video__play::after{content:"";position:absolute;left:8px;top:4px;border-left:7px solid var(--white);border-top:4px solid transparent;border-bottom:4px solid transparent}
.foot-a{left:0;right:0;top:468px;height:12px;background:var(--navy-mid)}
.foot-b{left:0;right:0;top:480px;height:15px;background:var(--navy)}

.note{position:absolute;font-family:"Gochi Hand",cursive;color:var(--note);font-size:17px}
.note--click{left:437px;top:78px;transform:rotate(-22deg)}
.note--opened{left:1050px;top:52px;transform:rotate(22deg)}
.arrows{position:absolute;left:0;top:0}
</style>
</head>
<body>

<section class="screen screen--closed">
  <div class="brand"><span class="brand__dot"></span><span class="brand__name">HARLOW &amp; REED</span></div>
  <div class="site-title">INTRANET</div>
  <div class="logout">logout (x)</div>
  <div class="topbar"></div>
  <div class="page"></div>
  <nav class="nav">
    <span class="nav__item">Home</span><span class="nav__item">Sales &amp;<br>Marketing</span><span class="nav__item">Customer<br>Service</span><span class="nav__item">Human<br>Resources</span><span class="nav__item">Information<br>Technology</span><span class="nav__item">Manufacturing</span><span class="nav__item">Finance &amp;<br>Accounting</span><span class="nav__item">Board of<br>Directors</span><span class="nav__item nav__item--wide">Admin</span><span class="nav__item nav__item--wide">Help</span>
  </nav>
  <div class="tab">My Personality</div>
  <article class="news">
    <div class="news__title">Announcements / News</div>
    <h3>Ridgeline Athletics accepts our proposal</h3>
    <p>Dan Whitford in our sales department recently announced that Ridgeline Athletics has approved our proposal to design and construct the manufacturing facilities in their new plant. Ridgeline is one of the top manufacturers of fitness equipment in the country. Dan said they considered proposals from seven other vendors before choosing Harlow &amp; Reed, stating that Ridgeline was impressed by the focus on quality and personal attention we provide.</p>
    <h3>Welcome to Clara Moss as shipping administrator</h3>
    <p>Clara Moss has joined us as shipping administrator in our Riverton office. She and her husband Neil live in Riverton and enjoy activities with their two daughters, Ella and Ivy.</p>
    <h3>Our new website is live</h3>
    <p>Brightline Systems has launched our new website, http://demo.brightline-sys.com. Owen Pratt said that BLS added several new features geared toward improving sales, including a Request for Quote form and a Refer a Friend tool.</p>
  </article>
  <div class="band"></div>
  <div class="card" style="left:3px">8.00-9.00 - Sam Keller<br>4.00-4.55 - Lena Brooks<br>and more scedule</div>
  <div class="card" style="left:143px">8.00-9.00 - Sam Keller<br>4.00-4.55 - Lena Brooks<br>and more scedule</div>
  <div class="card" style="left:283px">8.00-9.00 - Sam Keller<br>4.00-4.55 - Lena Brooks<br>and more scedule</div>
  <div class="video" style="left:428px" role="img" aria-label="Video still of the company CEO"><span class="video__play"></span></div>
  <div class="pill" style="left:10px"></div>
  <div class="pill" style="left:152px">Who's Out Today</div>
  <div class="pill" style="left:293px">Conference Rooms</div>
  <div class="pill" style="left:434px">Update from our CEO</div>
  <div class="foot-a"></div>
  <div class="foot-b"></div>
</section>

<section class="screen screen--open">
  <div class="brand"><span class="brand__dot"></span><span class="brand__name">HARLOW &amp; REED</span></div>
  <div class="site-title">INTRANET</div>
  <div class="logout" style="right:30px">logout (x)</div>
  <div class="topbar"></div>
  <div class="page"></div>
  <nav class="nav">
    <span class="nav__item">Home</span><span class="nav__item">Sales &amp;<br>Marketing</span><span class="nav__item">Customer<br>Service</span><span class="nav__item">Human<br>Resources</span><span class="nav__item">Information<br>Technology</span><span class="nav__item">Manufacturing</span><span class="nav__item">Finance &amp;<br>Accounting</span><span class="nav__item">Board of<br>Directors</span><span class="nav__item nav__item--wide">Admin</span><span class="nav__item nav__item--wide">Help</span>
  </nav>
  <div class="tab">My Personality</div>
  <article class="news">
    <div class="news__title">Announcements / News</div>
    <h3>Ridgeline Athletics accepts our proposal</h3>
    <p>Dan Whitford in our sales department recently announced that Ridgeline Athletics has approved our proposal to design and construct the manufacturing facilities in their new plant. Ridgeline is one of the top manufacturers of fitness equipment in the country. Dan said they considered proposals from seven other vendors before choosing Harlow &amp; Reed, stating that Ridgeline was impressed by the focus on quality and personal attention we provide.</p>
    <h3>Welcome to Clara Moss as shipping administrator</h3>
    <p>Clara Moss has joined us as shipping administrator in our Riverton office. She and her husband Neil live in Riverton and enjoy activities with their two daughters, Ella and Ivy.</p>
    <h3>Our new website is live</h3>
    <p>Brightline Systems has launched our new website, http://demo.brightline-sys.com. Owen Pratt said that BLS added several new features geared toward improving sales, including a Request for Quote form and a Refer a Friend tool.</p>
  </article>
  <aside class="personal">
    <div class="calendar">
      <div class="calendar__grid">
        <span class="calendar__day">Su</span><span class="calendar__day">Mo</span><span class="calendar__day">Tu</span><span class="calendar__day">We</span><span class="calendar__day">Th</span><span class="calendar__day">Fr</span><span class="calendar__day">Sa</span>
        <span class="calendar__blank"></span><span class="calendar__blank"></span><span class="calendar__blank"></span><span class="calendar__blank"></span><span class="calendar__blank"></span><span class="calendar__date calendar__date--busy">1</span><span class="calendar__date calendar__date--busy">2</span>
        <span class="calendar__date calendar__date--busy">3</span><span class="calendar__date calendar__date--busy">4</span><span class="calendar__date calendar__date--busy">5</span><span class="calendar__date calendar__date--busy">6</span><span class="calendar__date calendar__date--busy">7</span><span class="calendar__date">8</span><span class="calendar__date">9</span>
        <span class="calendar__date">10</span><span class="calendar__date">11</span><span class="calendar__date">12</span><span class="calendar__date">13</span><span class="calendar__date">14</span><span class="calendar__date calendar__date--busy">15</span><span class="calendar__date calendar__date--busy">16</span>
        <span class="calendar__date calendar__date--busy">17</span><span class="calendar__date calendar__date--busy">18</span><span class="calendar__date calendar__date--busy">19</span><span class="calendar__date">20</span><span class="calendar__date">21</span><span class="calendar__date">22</span><span class="calendar__date">23</span>
        <span class="calendar__date">24</span><span class="calendar__date">25</span><span class="calendar__date">26</span><span class="calendar__date">27</span><span class="calendar__date">28</span><span class="calendar__date">29</span><span class="calendar__date calendar__date--busy">30</span>
        <span class="calendar__date calendar__date--busy">31</span>
      </div>
      <div class="calendar__month">▲ march 2013 ▼</div>
    </div>
    <div class="actions">
      <span class="actions__btn">Employ Directory</span><span class="actions__btn">Vendor Directory</span>
      <span class="actions__btn">Trouble Ticket</span><span class="actions__btn">Leave Request</span>
    </div>
  </aside>
  <div class="band"></div>
  <div class="card" style="left:3px">8.00-9.00 - Sam Keller<br>4.00-4.55 - Lena Brooks<br>and more scedule</div>
  <div class="card" style="left:143px">8.00-9.00 - Sam Keller<br>4.00-4.55 - Lena Brooks<br>and more scedule</div>
  <div class="card" style="left:283px">8.00-9.00 - Sam Keller<br>4.00-4.55 - Lena Brooks<br>and more scedule</div>
  <div class="video" style="left:428px" role="img" aria-label="Video still of the company CEO"><span class="video__play"></span></div>
  <div class="pill" style="left:10px"></div>
  <div class="pill" style="left:152px">Who's Out Today</div>
  <div class="pill" style="left:293px">Conference Rooms</div>
  <div class="pill" style="left:434px">Update from our CEO</div>
  <div class="foot-a"></div>
  <div class="foot-b"></div>
</section>

<span class="note note--click">if i click this button</span>
<span class="note note--opened">this opened</span>
<svg class="arrows" width="1200" height="501" viewBox="0 0 1200 501" fill="none" stroke="#e2261f" stroke-width="3" stroke-linecap="round">
  <path d="M578 118 C582 130 578 140 568 147"/>
  <path d="M566 139 L567 148 L576 147"/>
  <path d="M580 112 C640 -10 1080 -20 1182 148"/>
  <path d="M1168 132 L1183 150 L1186 128"/>
</svg>

</body>
</html>
```